Austin Motivated Sellers #1

I am A local real estate investor in the highly competitive single family homes market of Austin,Tx.for fix and flipping My company uses several nontraditional and creative solutions for helping home owners sell their faster for cash with a closing date of their choice and helps them save thousands of dollars in having to pay real estate commissions and fees.My idea for the front of the postcard is to show the home owner what they could do with all the money they'll save by selling their home with us.I want a background picture on the front of taking a vacation with the money they'll save, or down payment on a new car on the back or even just a pile of cash they'll save to do whatever they like with.
Company name: Bold Harbor Properties
website: www.Quickdeedoffer.example
phone # : 512-555-0187 / 24hr.recorded message

Industry/Entity Type

Real Estate

```html
<!DOCTYPE html>
<html lang="en">
<head>
<meta charset="utf-8">
<title>Bold Harbor Properties – Postcard</title>
<link href="https://fonts.googleapis.com/css2?family=Barlow:wght@500;600;700&family=PT+Sans:wght@400;700&display=swap" rel="stylesheet">
<style>
  :root{
    --bg:#e4e5e7;
    --paper:#ffffff;
    --brick:#a8402f;
    --red:#d93a34;
    --purple:#3e3576;
    --sky:#1a86c8;
    --navy:#1d3f8c;
    --ink:#222222;
    --rule:#555555;
  }
  *{margin:0;padding:0;box-sizing:border-box}
  html,body{width:1089px;height:1200px;overflow:hidden;background:var(--bg)}
  body{position:relative;font-family:"PT Sans",sans-serif;color:var(--ink)}
  .card{position:absolute;left:134px;width:806px;height:539px;background:var(--paper)}
  .card--front{top:41px}
  .card--back{top:625px}

  .top-band{position:absolute;left:0;top:0;width:806px;height:54px;background:linear-gradient(90deg,var(--brick),var(--red))}
  .photo{position:absolute;top:63px;height:256px}
  .photo--vacation{left:0;width:395px;background:linear-gradient(180deg,#1f6fc4 0%,#5fa6dc 40%,#48b6c9 62%,#8a7f6c 100%)}
  .photo--car{left:405px;width:401px;background:linear-gradient(180deg,#c9b89d 0%,#a08866 45%,#6b6460 75%,#4a4a4c 100%)}

  .stripe{position:absolute;left:0;height:12px;display:flex}
  .stripe span{height:100%}
  .s-purple{background:var(--purple)}
  .s-brick{background:var(--brick)}
  .s-sky{background:var(--sky)}
  .stripe-line{position:absolute;left:0;height:5px;background:var(--sky)}

  .pitch{position:absolute;left:38px;top:402px;font-family:"Barlow",sans-serif;font-weight:600}
  .pitch__head{color:var(--brick);font-size:21.5px;line-height:1.2}
  .pitch__sub{color:var(--sky);font-size:17.5px;margin-top:6px}
  .pitch__call{color:var(--sky);font-size:17.5px;margin-top:9px}

  .brand{position:absolute;font-family:"Barlow",sans-serif;font-weight:600;color:var(--navy);text-align:center;line-height:1.1;display:flex;flex-direction:column;align-items:center}
  .brand__mark{width:14px;height:14px;background:var(--navy);margin-bottom:8px}
  .brand--front{left:640px;top:408px;width:140px;font-size:19px}
  .brand--back{left:566px;top:48px;width:128px;font-size:16px}

  .photo--sold{position:absolute;left:14px;top:39px;width:216px;height:248px;background:radial-gradient(ellipse at 50% 55%,#d9cbb2 0%,#b9c3b0 45%,#f2f2f2 80%,#ffffff 100%)}
  .copy{position:absolute;left:240px;top:35px;width:282px;font-size:10.6px;line-height:13.7px;text-align:justify}
  .copy p+p{margin-top:13px}
  .copy b{font-weight:700}

  .stamp{position:absolute;left:703px;top:37px;width:72px;height:85px;border:1px solid var(--rule)}
  .address-line{position:absolute;height:1px;background:var(--rule)}

  .offer{position:absolute;left:0;top:367px;width:522px;height:126px;background:linear-gradient(90deg,var(--brick),var(--red));color:#fff;font-family:"Barlow",sans-serif;font-weight:600;padding:18px 26px}
  .offer__head{font-size:18.5px;line-height:1.1}
  .offer__sub{font-size:14.5px;margin-top:2px}
  .offer__call{font-size:14.5px;margin-top:24px}
</style>
</head>
<body>

<section class="card card--front">
  <div class="top-band"></div>
  <div class="photo photo--vacation" role="img" aria-label="Tropical infinity pool deck with parasol and lounge chairs overlooking the sea"></div>
  <div class="photo photo--car" role="img" aria-label="Red electric sedan driving along a mountain road at sunset"></div>
  <div class="stripe" style="top:329px;width:806px">
    <span class="s-purple" style="width:194px"></span>
    <span class="s-brick" style="width:244px"></span>
    <span class="s-purple" style="width:55px"></span>
    <span class="s-sky" style="width:150px"></span>
    <span class="s-brick" style="width:163px"></span>
  </div>
  <div class="stripe-line" style="top:345px;width:806px"></div>

  <div class="pitch">
    <p class="pitch__head">You could save thousands selling your house with us...</p>
    <p class="pitch__sub">Enough for a nice vacation or a down payment on a new car!</p>
    <p class="pitch__call">Call today: 512-555-0187 / 24hr. recorded message</p>
  </div>

  <div class="brand brand--front"><span class="brand__mark"></span>Bold Harbor<br>Properties</div>
</section>

<section class="card card--back">
  <div class="photo--sold" role="img" aria-label="Model house on a pile of dollar bills with a SOLD sign"></div>

  <div class="copy">
    <p>Welcome...if you're <b>Looking to Sell Your Property</b> , you've come to the right place!</p>
    <p>We are a local cash buyer here in Austin and we use some creative and nontraditional solutions most realtors don't know about or won't tell you that can literally help you save thousands of dollars in expensive realtors commissions and fees.</p>
    <p>If you're like most sellers you want to explore how to sell your house fast and hassle free for the most money possible. Selling with us could save you thousands and we'll even buy your property as is so you won't need to make any repairs and you can even choose your move out date.</p>
    <p><b>We Buy Properties Fast</b>... regardless of condition, equity, or situation. We've handled just about every situation you can imagine. We buy with cash. We even have many creative solutions available. We are experts.</p>
  </div>

  <div class="brand brand--back"><span class="brand__mark"></span>Bold Harbor<br>Properties</div>
  <div class="stamp"></div>
  <div class="address-line" style="left:577px;top:221px;width:198px"></div>
  <div class="address-line" style="left:577px;top:270px;width:198px"></div>
  <div class="address-line" style="left:577px;top:318px;width:198px"></div>
  <div class="address-line" style="left:666px;top:367px;width:109px"></div>

  <div class="stripe" style="top:329px;width:522px">
    <span class="s-purple" style="width:121px"></span>
    <span class="s-brick" style="width:157px"></span>
    <span class="s-purple" style="width:35px"></span>
    <span class="s-sky" style="width:96px"></span>
    <span class="s-brick" style="width:113px"></span>
  </div>
  <div class="stripe-line" style="top:345px;width:522px"></div>

  <div class="offer">
    <p class="offer__head">You could save thousands selling your house with us...</p>
    <p class="offer__sub">Enough for a nice vacation or a down payment on a new car!</p>
    <p class="offer__call">Call today: 512-555-0187 / 24hr.recorded message</p>
  </div>
</section>

</body>
</html>
```